Business card design for immigration consulting business

We need business card design for a company called R&T Immigration Consultants Inc. This is a boutique immigration consulting and foreign recruitment agency owned and managed by two partners.
The business card will be used by partners \ owners of the business. The best way to describe the business would be committed to client, passionate about providing top-notch services, engaging, competent, professional

Target Market(s)

We work with individuals in and outside of Canada who need immigration advise as well as Canadian businesses looking to hire or sponsor foreign workers to Canada

Industry/Entity Type

Consulting

Contact Information for Business Card

The business card should have a standard size and horizontal lay-out

Font styles to use
Serif

Colors
f04a50
ec1f27
cbcbcb
dbdbdb

Requirements
Must have
• The business card mush have our logo, name of the company first and last name of the partner, position, phone, cell, fax, e-mail, skype, web-site
• Our first choice would a classic design with minimalist looks and elegant fonts and colors, but we are open minded to any creative ideas too
Nice to have
• On the other side it may have the description of the company: Immigration and Foreign Recruitment Services
• We're considering using stamping \ lettering on our business cards
• It would be nice if the business card would have white space, in case someone would like to make notes on it.
• One (back side) side of the business card can be all red with white logo
Should not have
• We do not want to have our pictures on the business card
• We do no want to have Canadian maple leaf on the business card as we already have one in our logo

```html
<!DOCTYPE html>
<html lang="en">
<head>
<meta charset="utf-8">
<title>R&amp;T Immigration Consultants Inc. – Business Card</title>
<link rel="stylesheet" href="https://fonts.googleapis.com/css2?family=Crimson+Pro:wght@400;600&display=swap">
<style>
  :root {
    --stage: #2a2a2c;
    --brand-red: #ec1f27;
    --accent-red: #f04a50;
    --ink-grey: #5e5e5e;
    --text-grey: #3f3f3f;
    --rule-grey: #cbcbcb;
    --paper: #ffffff;
    --paper-shade: #f3f3f3;
    --serif: "Crimson Pro", "Times New Roman", serif;
  }
  * { box-sizing: border-box; margin: 0; padding: 0; }
  html, body { width: 1200px; height: 903px; overflow: hidden; }
  body {
    background: var(--stage);
    font-family: var(--serif);
    position: relative;
  }
  .card {
    position: absolute;
    width: 620px;
    height: 354px;
    left: 290px;
    border-radius: 26px;
    overflow: hidden;
    box-shadow: 0 14px 30px rgba(0,0,0,.45);
  }
  /* Front: red side */
  .card--front {
    top: 64px;
    background: var(--brand-red);
    color: var(--paper);
  }
  .card--front .brand {
    position: absolute;
    left: 0;
    right: 0;
    top: 128px;
    text-align: center;
  }
  .brand-name {
    font-family: var(--serif);
    font-weight: 600;
    font-size: 56px;
    letter-spacing: 1px;
    line-height: 1;
    white-space: nowrap;
  }
  .card--front .brand-name { color: var(--paper); }
  .tagline {
    position: absolute;
    left: 0;
    right: 0;
    bottom: 42px;
    text-align: center;
    font-size: 20px;
    font-weight: 400;
    letter-spacing: .3px;
  }
  /* Back: white side */
  .card--back {
    top: 486px;
    background: linear-gradient(180deg, var(--paper) 0%, var(--paper-shade) 100%);
    display: flex;
    align-items: center;
  }
  .card--back .brand {
    width: 340px;
    padding: 0 30px 0 40px;
    display: flex;
    justify-content: center;
  }
  .card--back .brand-name {
    color: var(--ink-grey);
    font-size: 34px;
  }
  .divider {
    width: 1px;
    height: 180px;
    background: var(--rule-grey);
    flex: none;
  }
  .contact {
    padding-left: 32px;
    padding-right: 20px;
  }
  .person-name {
    font-size: 24px;
    font-weight: 600;
    color: var(--text-grey);
    line-height: 1.05;
  }
  .person-role {
    font-size: 16px;
    color: var(--brand-red);
    margin-bottom: 10px;
  }
  .contact-list { list-style: none; }
  .contact-item {
    display: flex;
    align-items: center;
    gap: 10px;
    font-size: 16px;
    color: var(--text-grey);
    height: 22px;
    white-space: nowrap;
  }
  .contact-icon { width: 17px; height: 17px; flex: none; }
</style>
</head>
<body>

  <section class="card card--front" aria-label="Card front">
    <div class="brand"><div class="brand-name">R&amp;T Immigration</div></div>
    <div class="tagline">Immigration and Foreign Recruitment Services</div>
  </section>

  <section class="card card--back" aria-label="Card back">
    <div class="brand"><div class="brand-name">R&amp;T Immigration</div></div>
    <div class="divider"></div>
    <div class="contact">
      <div class="person-name">Daniel Morvan</div>
      <div class="person-role">Managing Director</div>
      <ul class="contact-list">
        <li class="contact-item">
          <svg class="contact-icon" viewBox="0 0 20 20" aria-hidden="true"><circle cx="10" cy="10" r="10" fill="var(--brand-red)"/><path d="M6.5 5.5l2 2-1 1.2c.7 1.5 1.8 2.6 3.3 3.3l1.2-1 2 2-1.3 1.5c-3.8-.6-7-3.8-7.6-7.6z" fill="#fff"/></svg>
          +1 416 555 0142
        </li>
        <li class="contact-item">
          <svg class="contact-icon" viewBox="0 0 20 20" aria-hidden="true"><circle cx="10" cy="10" r="10" fill="var(--brand-red)"/><rect x="7" y="4.5" width="6" height="11" rx="1.2" fill="#fff"/><rect x="8" y="6" width="4" height="7" fill="var(--brand-red)"/></svg>
          +1 416 555 0187
        </li>
        <li class="contact-item">
          <svg class="contact-icon" viewBox="0 0 20 20" aria-hidden="true"><circle cx="10" cy="10" r="10" fill="var(--brand-red)"/><rect x="7" y="4.5" width="6" height="4" fill="#fff"/><rect x="5" y="8" width="10" height="5" rx="1" fill="#fff"/><rect x="7" y="11.5" width="6" height="4" fill="#fff" stroke="var(--brand-red)" stroke-width=".8"/></svg>
          +1 416 555 0193
        </li>
        <li class="contact-item">
          <svg class="contact-icon" viewBox="0 0 20 20" aria-hidden="true"><circle cx="10" cy="10" r="10" fill="var(--brand-red)"/><rect x="5" y="6.5" width="10" height="7" fill="#fff"/><path d="M5 6.5l5 4 5-4" fill="none" stroke="var(--brand-red)" stroke-width="1"/></svg>
          info@rtimmigration.ca
        </li>
        <li class="contact-item">
          <svg class="contact-icon" viewBox="0 0 20 20" aria-hidden="true"><circle cx="10" cy="10" r="10" fill="var(--brand-red)"/><g fill="none" stroke="#fff" stroke-width="1"><circle cx="10" cy="10" r="5"/><ellipse cx="10" cy="10" rx="2.2" ry="5"/><path d="M5 10h10M6 7.5h8M6 12.5h8"/></g></svg>
          www.rtimmigration.ca
        </li>
        <li class="contact-item">
          <svg class="contact-icon" viewBox="0 0 20 20" aria-hidden="true"><circle cx="10" cy="10" r="10" fill="var(--brand-red)"/><path d="M5 6h10v6H9l-3 2.5V12H5z" fill="#fff"/></svg>
          rt.immigration
        </li>
      </ul>
    </div>
  </section>

</body>
</html>
```